real estate business card
DR Horvath Company, Inc
Professional
Daniel Horvath
President
318 Birchwood St. #2207
Harlow Bay, ME 02196
Dan@drhorvathcompany.com
drhorvathcompany.com

```html
<!DOCTYPE html>
<html lang="en">
<head>
<meta charset="utf-8">
<title>DR Horvath Company, Inc – Business Card</title>
<link rel="stylesheet" href="https://fonts.googleapis.com/css2?family=Cinzel:wght@400;600&display=swap">
<style>
  :root {
    --bg: #d6d7d8;
    --paper: #ffffff;
    --brand-blue: #1f86c6;
    --brand-deep: #1660a8;
    --border-blue-a: #1565b3;
    --border-blue-b: #3fa6e2;
    --ink: #3a4450;
    --ink-soft: #6b7580;
    --rule: #9aa3ad;
    --faint: #e4eef6;
  }
  * { box-sizing: border-box; margin: 0; padding: 0; }
  html, body { width: 1200px; height: 895px; overflow: hidden; }
  body {
    background: var(--bg);
    font-family: "Cinzel", serif;
    color: var(--ink);
    position: relative;
  }
  .card {
    position: absolute;
    background: var(--paper);
    box-shadow: 0 10px 28px rgba(0,0,0,0.18);
  }

  /* Back card */
  .card-back {
    left: 620px; top: 80px;
    width: 540px; height: 310px;
    display: flex; align-items: center; justify-content: center;
  }
  .back-mark {
    display: flex; align-items: center; gap: 14px;
  }
  .back-mark .dot {
    width: 80px; height: 80px; border-radius: 50%;
    background: var(--faint);
    flex: none;
  }
  .back-mark .company {
    font-size: 24px; font-weight: 400; color: var(--brand-blue);
    letter-spacing: 1px; white-space: nowrap;
  }

  /* Front card */
  .card-front {
    left: 50px; top: 430px;
    width: 580px; height: 350px;
    padding: 14px;
    background: linear-gradient(135deg, var(--border-blue-a), var(--border-blue-b));
  }
  .card-front .face {
    width: 100%; height: 100%;
    background: var(--paper);
    position: relative;
    padding: 40px 24px 0 36px;
  }
  .brand {
    display: flex; align-items: center; gap: 14px;
  }
  .brand .dot {
    width: 78px; height: 78px; border-radius: 50%;
    background: linear-gradient(160deg, var(--border-blue-b), var(--brand-deep));
    flex: none;
  }
  .brand .company {
    font-size: 26px; font-weight: 400; color: var(--brand-blue);
    letter-spacing: 1px; white-space: nowrap;
  }
  .details {
    position: absolute; left: 36px; right: 24px; top: 158px;
    display: flex; gap: 16px;
  }
  .person {
    width: 210px; text-align: right; padding-right: 16px;
    border-right: 1.5px solid var(--rule);
    font-size: 13.5px; line-height: 1.5;
    white-space: nowrap;
  }
  .person .name { color: var(--brand-blue); font-size: 16px; font-weight: 600; }
  .person .title { color: var(--ink-soft); margin-bottom: 4px; }
  .contact { list-style: none; font-size: 13px; line-height: 1.55; white-space: nowrap; }
  .contact li { display: flex; align-items: center; gap: 8px; }
  .contact svg { width: 14px; height: 14px; flex: none; }
</style>
</head>
<body>

  <section class="card card-back" aria-label="Business card back">
    <div class="back-mark">
      <span class="dot"></span>
      <span class="company">DR Horvath Company, Inc</span>
    </div>
  </section>

  <section class="card card-front" aria-label="Business card front">
    <div class="face">
      <div class="brand">
        <span class="dot"></span>
        <span class="company">DR Horvath Company, Inc</span>
      </div>

      <div class="details">
        <div class="person">
          <div class="name">Daniel Horvath</div>
          <div class="title">President</div>
          <div>318 Birchwood St. #2207</div>
          <div>Harlow Bay, ME 02196</div>
        </div>
        <ul class="contact">
          <li>
            <svg viewBox="0 0 14 14"><circle cx="7" cy="7" r="7" fill="#3a4450"/><path d="M4.3 3.6l1.4-.2.7 1.7-.9.6a5 5 0 0 0 2.8 2.8l.6-.9 1.7.7-.2 1.4c-3.4.2-6.3-2.7-6.1-6.1z" fill="#fff"/></svg>
            1-877-555-0148
          </li>
          <li>
            <svg viewBox="0 0 14 14"><circle cx="7" cy="7" r="7" fill="#3a4450"/><rect x="3.5" y="5" width="7" height="4.5" rx=".6" fill="#fff"/><rect x="5" y="3.3" width="4" height="2" fill="#fff"/></svg>
            508-555-0173
          </li>
          <li>
            <svg viewBox="0 0 14 14"><circle cx="7" cy="7" r="7" fill="#3a4450"/><rect x="3.4" y="4.4" width="7.2" height="5.2" fill="#fff"/><path d="M3.4 4.4L7 7.4l3.6-3" stroke="#3a4450" stroke-width=".8" fill="none"/></svg>
            Dan@drhorvathcompany.com
          </li>
          <li>
            <svg viewBox="0 0 14 14"><circle cx="7" cy="7" r="7" fill="#3a4450"/><circle cx="7" cy="7" r="3.6" fill="none" stroke="#fff" stroke-width=".9"/><path d="M3.4 7h7.2M7 3.4c-1.6 2-1.6 5.2 0 7.2M7 3.4c1.6 2 1.6 5.2 0 7.2" stroke="#fff" stroke-width=".8" fill="none"/></svg>
            www.drhorvathcompany.com
          </li>
        </ul>
      </div>
    </div>
  </section>

</body>
</html>
```